Vantrex Activated Carbon (coal-based)

The packaging for granular activated carbon must have a simple industrial concept but looks classy. Industrial look, bold and credible, also eye catching. Weight: 25 kg

Target Market(s)

Industrial

Industry/Entity Type

Water Treatment Industry

Requirements
Must have
• Weight : 25 kg, must have "coal-based", warning symbol in packaging
Nice to have
• There is a picture of granular activated carbon (coal-based) on the package

```html
<!DOCTYPE html>
<html lang="en">
<head>
<meta charset="utf-8">
<title>Vantrex Activated Carbon – 25 kg bag dieline</title>
<link href="https://fonts.googleapis.com/css2?family=Montserrat:wght@400;600;800;900&family=Cairo:wght@600&display=swap" rel="stylesheet">
<style>
  :root{
    --bg:#f2f1ef;
    --bag:#0d0d0d;
    --orange:#f26a21;
    --orange-light:#ff8a3d;
    --white:#ffffff;
    --grey:#a8a8a8;
    --line:#c9c9c9;
  }
  *{box-sizing:border-box;margin:0;padding:0}
  html,body{width:789px;height:1200px;overflow:hidden;background:var(--bg);font-family:"Montserrat",sans-serif}
  .canvas{position:relative;width:789px;height:1200px}
  .dieline{position:absolute;left:24px;top:290px;width:740px;height:620px;background:var(--bag);outline:1px solid var(--line);outline-offset:10px}
  .panel{position:absolute;top:0;height:100%}
  .panel--front{left:0;width:300px}
  .panel--back{left:370px;width:300px}
  .gusset{position:absolute;top:0;height:100%;width:70px;background:var(--orange);display:flex;align-items:center;justify-content:center}
  .gusset--left{left:300px}
  .gusset--right{left:670px}
  .gusset__text{transform:rotate(-90deg);white-space:nowrap;font-weight:900;font-size:20px;color:var(--bag);letter-spacing:1px}
  .gusset__text span{color:var(--white)}
  .granules{position:absolute;width:150px;height:170px;background:radial-gradient(circle at 40% 40%,var(--orange-light),var(--orange) 55%,rgba(242,106,33,0) 75%);clip-path:polygon(25% 0,75% 0,100% 50%,75% 100%,25% 100%,0 50%)}
  .panel--front .granules{right:14px;top:60px}
  .panel--back .granules{left:14px;top:60px}
  .brand{position:absolute;left:22px;font-weight:900;font-size:44px;line-height:1;color:var(--orange);letter-spacing:-.5px}
  .brand span{color:var(--white)}
  .sub{position:absolute;left:22px;font-size:10px;font-weight:600;color:var(--grey);letter-spacing:2px}
  .badge{position:absolute;left:22px;display:flex;align-items:center;gap:6px;font-weight:800;font-size:13px;color:var(--white)}
  .badge__tag{background:var(--orange);color:var(--bag);padding:2px 6px;font-size:11px}
  .copy{position:absolute;left:22px;width:200px;font-size:8.5px;line-height:1.45;color:var(--grey)}
  .icons{position:absolute;left:22px;display:flex;gap:8px}
  .icons svg{width:24px;height:24px}
  .label-box{position:absolute;left:22px;bottom:40px;width:110px;height:34px;background:var(--white)}
  .arabic{position:absolute;left:22px;font-family:"Cairo",sans-serif;font-size:15px;color:var(--white)}
  .weight-tab{position:absolute;right:0;bottom:70px;background:var(--orange);color:var(--bag);font-weight:900;font-size:22px;padding:6px 14px}
  .note{position:absolute;left:22px;bottom:40px;width:150px;font-size:8px;color:var(--grey);line-height:1.4}
</style>
</head>
<body>
<div class="canvas">
  <div class="dieline">
    <section class="panel panel--front">
      <div class="granules" role="img" aria-label="Granular activated carbon imagery in orange tones"></div>
      <div class="brand" style="top:250px">VAN<span>TREX</span></div>
      <div class="sub" style="top:300px">COAL-BASED</div>
      <div class="badge" style="top:318px"><span class="badge__tag">PREMIUM</span>ACTIVATED CARBON</div>
      <p class="copy" style="top:350px">Coal-based granular carbon for water treatment. Removes chlorine, odour and organic matter.</p>
      <div class="icons" style="top:400px">
        <svg viewBox="0 0 24 24"><path d="M12 3 22 20H2Z" fill="none" stroke="#f26a21" stroke-width="2"/><path d="M12 9v5M12 16v2" stroke="#f26a21" stroke-width="2"/></svg>
        <svg viewBox="0 0 24 24"><circle cx="12" cy="12" r="10" fill="none" stroke="#ffffff" stroke-width="1.5"/><path d="M12 6c3 4 4 6 4 8a4 4 0 0 1-8 0c0-2 1-4 4-8z" fill="#ffffff"/></svg>
        <svg viewBox="0 0 24 24"><circle cx="12" cy="12" r="10" fill="none" stroke="#ffffff" stroke-width="1.5"/><path d="M7 12l3 3 7-7" fill="none" stroke="#ffffff" stroke-width="2"/></svg>
        <svg viewBox="0 0 24 24"><rect x="3" y="3" width="18" height="18" fill="none" stroke="#ffffff" stroke-width="1.5"/><path d="M8 16h8M12 7v9" stroke="#ffffff" stroke-width="2"/></svg>
      </div>
      <div class="sub" style="top:432px;letter-spacing:1px">Warning</div>
      <div class="label-box"></div>
    </section>

    <div class="gusset gusset--left"><div class="gusset__text"><span>PREMIUM</span> ACTIVATED CARBON</div></div>

    <section class="panel panel--back">
      <div class="granules" role="img" aria-label="Granular activated carbon imagery in orange tones"></div>
      <div class="brand" style="top:250px">VAN<span>TREX</span></div>
      <div class="sub" style="top:300px">COAL-BASED</div>
      <div class="badge" style="top:318px"><span class="badge__tag">PREMIUM</span>ACTIVATED CARBON</div>
      <div class="arabic" style="top:344px">كربون منشط</div>
      <p class="copy" style="top:378px">Store sealed in a cool dry place. Avoid dust inhalation.</p>
      <div class="weight-tab">25 KG</div>
      <p class="note">For industrial water treatment use only.</p>
    </section>

    <div class="gusset gusset--right"><div class="gusset__text"><span>PREMIUM</span> ACTIVATED CARBON</div></div>
  </div>
</div>
</body>
</html>
```